Cover needed for Tunevault/plimbra/digital release

Cover design needed for a Reggae song to be released as a single on tunevault/ disc mango/ plimbra/ vidhollow etc... for the artist it should say Marcus Delvane Meets Bluffmoors and the song: Sway Down Low Now. At the top it should say Marcus Delvane and (Meets Bluffmoors) can be in smaller letters. and the song title towards the bottom. Plus I would also like the same cover done without (Meets Bluffmoors) included in the picture. So in total 2 images. The image theme can be reggae/ dancehall/ rub a dub/ vinyl turntable related. Here is some information about the image quality that the website I am using wants it in:
1400 x 1400 pixels minimum; 3000 x 3000 pixels maximum
PNG, GIF, JPG, or JPEG file type
72 - 300dpi (300dpi is the best)
Less than 25mb
RGB color scheme (not CMYK)
Unique to this particular title. We cannot accept artwork that has been used for another title.
Uploaded image must match your physical album cover artwork.
IMPORTANT: If your artist name and the title of your album or single appear on your cover artwork, it MUST precisely match the information you provided for this project. The text should be identical. For instance, if the artist name you provided is "Pellow & Rundquist (featuring Varn & Bettick)," the text on your artwork should NOT say "Pellow and Rundquist."
Updates
I upgraded to be able to choose from more designs. Thank You
Target Market(s)
target market: Just Reggae fans dub fans, rub a dub/dancehall fans,

```html
<!DOCTYPE html>
<html lang="en">
<head>
<meta charset="utf-8">
<title>Marcus Delvane – Sway Down Low Now</title>
<link href="https://fonts.googleapis.com/css2?family=Permanent+Marker&display=swap" rel="stylesheet">
<style>
  :root {
    --paper: #eeeadb;
    --paper-shade: #e2dcc8;
    --rasta-green: #2f8a1c;
    --leaf-green: #5fc224;
    --rasta-gold: #c9a817;
    --sun-yellow: #f2d21a;
    --rasta-red: #c62516;
    --deep-red: #a8190f;
  }
  html, body {
    margin: 0;
    padding: 0;
    width: 1200px;
    height: 1200px;
    overflow: hidden;
  }
  .cover {
    position: relative;
    width: 1200px;
    height: 1200px;
    overflow: hidden;
    background:
      radial-gradient(ellipse at 30% 40%, rgba(255,255,255,0.55), transparent 55%),
      radial-gradient(ellipse at 75% 70%, rgba(200,190,160,0.25), transparent 50%),
      radial-gradient(ellipse at 15% 85%, rgba(190,180,150,0.25), transparent 45%),
      var(--paper);
    font-family: 'Permanent Marker', cursive;
  }
  .paint-strokes {
    position: absolute;
    inset: 0;
    width: 1200px;
    height: 1200px;
  }
  .typeset {
    position: absolute;
    left: 0;
    top: 0;
    width: 1200px;
    height: 1200px;
    transform: rotate(6deg);
    transform-origin: 600px 600px;
  }
  .artist {
    position: absolute;
    left: 215px;
    top: 150px;
    margin: 0;
    font-size: 50px;
    line-height: 1;
    letter-spacing: -1px;
    color: var(--rasta-green);
    white-space: nowrap;
    font-weight: 400;
  }
  .artist .feature {
    font-size: 34px;
  }
  .artist-rule {
    position: absolute;
    left: 230px;
    top: 218px;
    width: 640px;
    height: 9px;
    background: var(--rasta-green);
    border-radius: 4px;
  }
  .title {
    position: absolute;
    left: 0;
    top: 230px;
    width: 1200px;
    margin: 0;
    text-align: center;
    font-size: 232px;
    line-height: 0.93;
    font-weight: 400;
    letter-spacing: -4px;
    color: transparent;
    background: linear-gradient(180deg,
      var(--leaf-green) 0px, var(--rasta-green) 230px,
      var(--rasta-gold) 230px, var(--sun-yellow) 420px, var(--rasta-gold) 540px,
      var(--rasta-red) 540px, var(--deep-red) 760px);
    -webkit-background-clip: text;
    background-clip: text;
  }
  .title span {
    display: block;
  }
</style>
</head>
<body>
<main class="cover">
  <svg class="paint-strokes" viewBox="0 0 1200 1200" role="img" aria-label="Green, yellow and red rasta brush strokes in the corners">
    <defs>
      <linearGradient id="strokeTop" x1="0" y1="0" x2="0" y2="1">
        <stop offset="0" stop-color="#f2d21a"/>
        <stop offset="0.45" stop-color="#7cc928"/>
        <stop offset="1" stop-color="#3a9a1c"/>
      </linearGradient>
      <radialGradient id="strokeYellow" cx="0.3" cy="0.6" r="0.7">
        <stop offset="0" stop-color="#f2a515"/>
        <stop offset="0.6" stop-color="#f5d81e"/>
        <stop offset="1" stop-color="#f5e04a" stop-opacity="0"/>
      </radialGradient>
      <linearGradient id="strokeBottom" x1="0" y1="0" x2="0.3" y2="1">
        <stop offset="0" stop-color="#6cc42a"/>
        <stop offset="0.3" stop-color="#e3a51a"/>
        <stop offset="0.55" stop-color="#d9431b"/>
        <stop offset="1" stop-color="#b81a10"/>
      </linearGradient>
    </defs>
    <path d="M200 0 L1200 0 L1200 75 L1130 110 L950 150 L700 105 L450 55 L230 20 Z" fill="url(#strokeTop)"/>
    <path d="M0 965 Q120 950 190 1010 Q230 1090 200 1200 L0 1200 Z" fill="url(#strokeYellow)"/>
    <path d="M840 1030 L1200 880 L1200 1200 L810 1200 L880 1110 Z" fill="url(#strokeBottom)"/>
  </svg>

  <div class="typeset">
    <p class="artist">MARCUS DELVANE <span class="feature">(&amp; MEETS BLUFFMOORS)</span></p>
    <div class="artist-rule"></div>
    <h1 class="title">
      <span>SWAY</span>
      <span>DOWN</span>
      <span>LOW NOW</span>
    </h1>
  </div>
</main>
</body>
</html>
```